Bright Fern Custom Homes business card. Double sided. Modern. professional

Bright Fern Custom Homes
contemporary modern design with our logo /
Double sided with all our contact information
Use same Green colors as in our Logo. Contemporary logo that grabs your attention. Visually pleasing and balanced. Easy to read, and Vibrant. Would love an option for rounded edges. Embossed logo would be amazing.
Contact Information for Business Card
Dana Welk Owner / General Contractor Bright Fern Custom Homes p: 704.552.1830 m: 912.648.2071 e: brightferncustomhomes@mailbox.example w: www.brightferncustomhomes.example 218 Pryor Meadow Lane Marlow Ridge, SC 29041

```html
<!DOCTYPE html>
<html lang="en">
<head>
<meta charset="utf-8">
<title>Bright Fern Custom Homes – Business Card</title>
<link rel="stylesheet" href="https://fonts.googleapis.com/css2?family=Cinzel:wght@500&family=Montserrat:wght@500&family=Roboto:wght@400;700&display=swap">
<style>
  :root {
    --backdrop: #adadad;
    --card-green: #5c6e31;
    --brand-deep: #45541f;
    --brand-green: #5a6f2c;
    --brand-light: #7a9a3c;
    --paper: #ffffff;
    --ink: #111111;
  }
  * { margin: 0; padding: 0; box-sizing: border-box; }
  html, body { width: 1200px; height: 1000px; overflow: hidden; }
  body { background: var(--backdrop); position: relative; font-family: "Roboto", Arial, sans-serif; }

  .card {
    position: absolute;
    width: 612px;
    height: 352px;
    border-radius: 22px;
    overflow: hidden;
  }
  .card-front { left: 299px; top: 79px; background: var(--card-green); }
  .card-back  { left: 294px; top: 537px; background: var(--paper); }

  .front-mark {
    position: absolute;
    left: 236px; top: 50px;
    width: 150px; height: 150px;
    border-radius: 50%;
    background: var(--brand-deep);
  }
  .front-wordmark {
    position: absolute;
    left: 0; right: 0; top: 248px;
    text-align: center;
    font-family: "Cinzel", Georgia, serif;
    font-weight: 500;
    color: var(--brand-deep);
    line-height: 1;
  }
  .front-wordmark .name-main { display: block; font-size: 40px; letter-spacing: 1px; }
  .front-wordmark .name-sub  { display: block; margin-top: 4px; font-size: 12px; letter-spacing: 6px; }

  .holder { position: absolute; left: 44px; top: 96px; }
  .holder-name {
    font-family: "Cinzel", Georgia, serif;
    font-weight: 500;
    font-size: 31px;
    color: var(--brand-green);
    line-height: 1;
  }
  .holder-role {
    margin-top: 8px;
    padding-left: 55px;
    font-family: "Montserrat", Arial, sans-serif;
    font-weight: 500;
    font-size: 15px;
    letter-spacing: 2.5px;
    color: var(--brand-light);
  }
  .contact {
    position: absolute;
    left: 44px; top: 187px;
    font-size: 15px;
    line-height: 19.5px;
    color: var(--ink);
    list-style: none;
  }
  .contact b { font-weight: 700; }
  .address {
    position: absolute;
    left: 44px; top: 283px;
    font-size: 15px;
    line-height: 21px;
    color: var(--ink);
    font-style: normal;
  }
  .back-mark {
    position: absolute;
    left: 372px; top: 36px;
    width: 220px; height: 220px;
    border-radius: 50%;
    background: linear-gradient(135deg, var(--brand-green), var(--brand-light));
  }
</style>
</head>
<body>
  <section class="card card-front">
    <div class="front-mark" role="img" aria-label="Company mark"></div>
    <div class="front-wordmark">
      <span class="name-main">BRIGHT FERN</span>
      <span class="name-sub">CUSTOM HOMES</span>
    </div>
  </section>

  <section class="card card-back">
    <div class="holder">
      <div class="holder-name">Dana Welk</div>
      <div class="holder-role">OWNER</div>
    </div>
    <ul class="contact">
      <li><b>p:</b> 704.552.1830</li>
      <li><b>m:</b> 912.648.2071</li>
      <li><b>e:</b> brightferncustomhomes@mailbox.example</li>
      <li><b>w:</b> brightferncustomhomes.example</li>
    </ul>
    <address class="address">218 Pryor Meadow Lane,<br>Marlow Ridge, SC 29041</address>
    <div class="back-mark" role="img" aria-label="Company mark"></div>
  </section>
</body>
</html>
```